The Seeds Of Quiet Harvest Inc.

On one side have the business name. On the other side have contact information. This is an indoor cannabis cultivation business. It’s a new company in Sacramento ca. So we need a logo designed. The company is Called the seeds of quiet harvest. We grow and distribute marijuana in California. We would like to see designers use the color green and communicate cultivation.

Target Market(s)

Networking

Contact Information for Business Card

Brent Tavaro: president
Phone: (916) 555-0147
Email: brent@theseedsofquietharvest.net

Logo Text

Not sure if i want text or just an image created by designers.

Font styles to use
Script

Colors
000000
9bcb3c
fbfcf7
cadf82

Requirements
Nice to have
• A classic elegant professional card.

```html
<!DOCTYPE html>
<html lang="en">
<head>
<meta charset="utf-8">
<title>The Seeds Of Quiet Harvest Inc. — Business Card</title>
<link rel="stylesheet" href="https://fonts.googleapis.com/css2?family=Yellowtail&family=Roboto:wght@400&display=swap">
<style>
  :root {
    --stage: #3a3a3a;
    --card: #141414;
    --card-edge: #0a0a0a;
    --green: #9bcb3c;
    --green-soft: #cadf82;
    --ink: #000000;
    --paper: #fbfcf7;
  }
  * { margin: 0; padding: 0; box-sizing: border-box; }
  html, body {
    width: 1200px;
    height: 960px;
    overflow: hidden;
    background: var(--stage);
  }
  .stage {
    position: relative;
    width: 1200px;
    height: 960px;
  }
  .card {
    position: absolute;
    width: 580px;
    height: 330px;
    background: var(--card);
    border-radius: 26px;
    box-shadow: 0 3px 0 var(--card-edge), 0 6px 0 #1c1c1c, 0 9px 0 var(--card-edge);
    color: var(--green);
    font-family: "Roboto", Arial, sans-serif;
    display: flex;
    flex-direction: column;
    align-items: center;
    justify-content: center;
    text-align: center;
  }
  .card--front { left: 90px; top: 110px; }
  .card--back { left: 530px; top: 510px; }

  .brand {
    display: flex;
    align-items: center;
    gap: 12px;
  }
  .brand__mark {
    width: 26px;
    height: 26px;
    background: var(--green);
  }
  .brand__name {
    font-size: 26px;
    font-weight: 400;
    line-height: 1.2;
    color: var(--green);
  }
  .location {
    margin-top: 14px;
    font-size: 20px;
    font-weight: 400;
    letter-spacing: 1px;
    color: var(--green);
  }
  .website {
    margin-top: 34px;
    font-size: 15px;
    letter-spacing: 2px;
    color: var(--green);
  }

  .contact__name {
    font-family: "Yellowtail", cursive;
    font-size: 40px;
    line-height: 1.1;
  }
  .contact__role {
    font-size: 20px;
    margin-top: 2px;
  }
  .contact__rule {
    width: 54px;
    height: 2px;
    background: var(--green);
    margin: 12px 0 16px;
  }
  .contact__line {
    font-size: 21px;
    line-height: 1.3;
  }
</style>
</head>
<body>
  <main class="stage">
    <section class="card card--front" aria-label="Card front">
      <div class="brand">
        <span class="brand__mark"></span>
        <span class="brand__name">The Seeds Of Quiet Harvest Inc.</span>
      </div>
      <p class="location">Sacramento ca.</p>
      <p class="website">www.yourwebsite.com</p>
    </section>

    <section class="card card--back" aria-label="Card back">
      <p class="contact__name">Brent Tavaro</p>
      <p class="contact__role">President</p>
      <span class="contact__rule"></span>
      <p class="contact__line">(916) 555-0147</p>
      <p class="contact__line">brent@theseedsofquietharvest.net</p>
    </section>
  </main>
</body>
</html>
```